Business cards and logo for kitchen and bath remodeling company

We want an elegant card but that calls attention something unique and when people see it they remember us. A log that we can use for our own. We are a kitchen and bathroom remodeling company. We are 3 partners staring the company we are located in seattle washington usa. We try to give the best experience and luxury look in our projects and we are looking to show that in our cards. I added a sample of a card I really like. I like the black and gold look but gray blue or green in a metallic look would look nice. I'm open to any color.

Target Market(s)

Home owners.

Industry/Entity Type

Construction

Contact Information for Business Card

Copperfern builders

Colors

Designer to choose colors to be used in the design.

Requirements
Must have
• Make a Logo
• Logo to be unique
• Name of company copperfern builders
Nice to have
• Have a good color scheme
• Front design to connect with back of card

```html
<!DOCTYPE html>
<html lang="en">
<head>
<meta charset="utf-8">
<title>Copperfern Builders – Business Card</title>
<link href="https://fonts.googleapis.com/css2?family=Montserrat:wght@300;400;600;700&display=swap" rel="stylesheet">
<style>
  :root {
    --backdrop: #b8946a;
    --paper: #f7f7f5;
    --slate: #3b3e45;
    --slate-deep: #2f3238;
    --gold: #b8892e;
    --gold-light: #d9b55a;
    --ink: #2b2b2e;
    --ink-soft: #55565a;
    --rule: #3a3a3d;
  }
  * { box-sizing: border-box; margin: 0; padding: 0; }
  html, body { width: 1200px; height: 859px; overflow: hidden; }
  body {
    background: var(--backdrop);
    font-family: "Montserrat", sans-serif;
    position: relative;
  }
  .card {
    position: absolute;
    top: 289px;
    width: 501px;
    height: 284px;
    overflow: hidden;
  }
  .card--front { left: 60px; background: var(--paper); }
  .card--back {
    left: 639px;
    background: radial-gradient(ellipse at 45% 35%, var(--slate) 0%, var(--slate-deep) 100%);
  }

  .brand {
    position: absolute;
    display: flex;
    flex-direction: column;
    align-items: center;
    text-align: center;
  }
  .brand__square {
    width: 34px;
    height: 34px;
    background: var(--gold);
    margin-bottom: 14px;
  }
  .brand__name {
    font-weight: 700;
    text-transform: uppercase;
    line-height: 1.15;
    letter-spacing: 0.02em;
  }
  .brand__rule {
    display: flex;
    align-items: center;
    gap: 6px;
    margin-top: 3px;
  }
  .brand__rule::before, .brand__rule::after {
    content: "";
    display: block;
    width: 46px;
    height: 1.5px;
    background: currentColor;
  }

  .card--front .brand { left: 22px; top: 86px; width: 194px; }
  .card--front .brand__name { font-size: 15.5px; color: var(--ink); }
  .card--front .brand__rule { color: var(--rule); }

  .card--back .brand { left: 120px; top: 78px; width: 261px; }
  .card--back .brand__square { width: 42px; height: 42px; background: var(--gold-light); margin-bottom: 18px; }
  .card--back .brand__name { font-size: 20px; color: var(--gold-light); }
  .card--back .brand__rule { color: #9a9ba0; }
  .card--back .brand__rule::before, .card--back .brand__rule::after { width: 62px; }

  .holder {
    position: absolute;
    left: 267px;
    top: 86px;
    font-weight: 700;
    font-size: 15px;
    letter-spacing: 0.04em;
    color: var(--gold);
    text-transform: uppercase;
  }
  .contacts {
    position: absolute;
    left: 266px;
    top: 149px;
    list-style: none;
  }
  .contacts li {
    display: flex;
    align-items: center;
    gap: 6px;
    font-weight: 300;
    font-size: 12.5px;
    color: var(--ink-soft);
    height: 17.5px;
  }
  .contacts svg { width: 11px; height: 11px; flex: none; }

  .accent-bar {
    position: absolute;
    left: 0;
    bottom: 0;
    width: 241px;
    height: 9px;
    background: linear-gradient(90deg, var(--gold) 0%, var(--gold-light) 50%, var(--gold) 100%);
    clip-path: polygon(0 0, 236px 0, 100% 100%, 0 100%);
  }
</style>
</head>
<body>
  <section class="card card--front">
    <div class="brand">
      <span class="brand__square"></span>
      <span class="brand__name">Copperfern</span>
      <span class="brand__rule"><span class="brand__name">Builders</span></span>
    </div>

    <p class="holder">Marisol Vendrano</p>

    <ul class="contacts">
      <li>
        <svg viewBox="0 0 12 12" fill="none" stroke="#b8892e" stroke-width="1.1"><circle cx="6" cy="6" r="5"/><path d="M4.2 3.5 5 5l-.6.6a3.5 3.5 0 0 0 2 2l.6-.6 1.5.8-.5 1A4.8 4.8 0 0 1 3.2 4Z"/></svg>
        206 555 0147
      </li>
      <li>
        <svg viewBox="0 0 12 12" fill="none" stroke="#b8892e" stroke-width="1.1"><rect x="1" y="2.5" width="10" height="7"/><path d="M1 2.5 6 6.5l5-4"/></svg>
        hello@copperfernbuilders.com
      </li>
      <li>
        <svg viewBox="0 0 12 12" fill="none" stroke="#b8892e" stroke-width="1"><circle cx="6" cy="6" r="5"/><ellipse cx="6" cy="6" rx="2.2" ry="5"/><path d="M1 6h10M2 3.5h8M2 8.5h8"/></svg>
        copperfernbuilders.com
      </li>
    </ul>

    <span class="accent-bar"></span>
  </section>

  <section class="card card--back">
    <div class="brand">
      <span class="brand__square"></span>
      <span class="brand__name">Copperfern</span>
      <span class="brand__rule"><span class="brand__name">Builders</span></span>
    </div>
  </section>
</body>
</html>
```